Wild Mo's Wine Label Project

We need a new entry level wine label called "Wild Mo's" for a range of wines we are developing from inland Australia. Our company is made up of three youngish guys who live hard and love taking the mickey. Wild Mo is Wild Moss - the largest and loudest of the three partners (and ideally this label will take the mickey out of him). We've grown the grapes ourselves for this first release which will be a 2012 Pinot Gris. Wine style is dry, young, fresh and contemporary and pitched at the sub AUD $10 retail price point. The package will be flint (clear) claret shape bottle with plain screwcap (colour matched to suit the winning label design).

I've attached a couple of photos of Wild Moss to give you some idea of his presence and persona.

Target Market(s)

Semi educated 25 - 40 year old wine drinkers. Skewed towards females.

Industry/Entity Type

Retail

Requirements
Should not have
• Anything traditional or old fashioned

```html
<!DOCTYPE html>
<html lang="en">
<head>
<meta charset="utf-8">
<title>Wild Mo's 2012 – Label Range</title>
<link rel="stylesheet" href="https://fonts.googleapis.com/css2?family=Stardos+Stencil:wght@700&family=Arimo:wght@400&display=swap">
<style>
  :root {
    --label-blue: #3f7db3;
    --cap-blue: #3a78ae;
    --cap-blue-dark: #2c5f8c;
    --label-white: #ffffff;
    --glass-edge: #6e5e26;
    --glass-mid: #b9a55c;
    --glass-light: #e2d59c;
    --glass-base: #4a3f1a;
    --vine-gold-light: #d8a84e;
    --vine-gold-dark: #96681e;
    --vine-blue-light: #5a95c7;
    --vine-blue-dark: #346ea0;
    --vine-white-light: #ffffff;
    --vine-white-dark: #e4edf6;
    --canvas: #ffffff;
  }
  * { box-sizing: border-box; margin: 0; padding: 0; }
  html, body {
    width: 1200px;
    height: 3117px;
    overflow: hidden;
    background: var(--canvas);
  }
  .range {
    position: relative;
    width: 1200px;
    height: 3117px;
  }

  /* Bottle */
  .bottle {
    position: absolute;
    width: 460px;
    height: 1490px;
  }
  .bottle--top-left     { left: 110px; top: 59px; }
  .bottle--top-right    { left: 665px; top: 59px; }
  .bottle--bottom-left  { left: 110px; top: 1621px; }
  .bottle--bottom-right { left: 665px; top: 1621px; }
  .bottle svg { display: block; }
  .capsule-name {
    font-family: "Stardos Stencil", "Arial Black", sans-serif;
    font-weight: 700;
    font-size: 26px;
    fill: var(--label-white);
  }

  /* Label */
  .label {
    position: absolute;
    width: 424px;
    height: 488px;
    border-radius: 22px;
    border: 5px solid var(--label-blue);
    overflow: hidden;
  }
  .label--white { background: var(--label-white); }
  .label--blue  { background: var(--label-blue); }

  .label--top-left     { left: 128px; top: 973px; }
  .label--top-right    { left: 683px; top: 973px; }
  .label--bottom-left  { left: 128px; top: 2545px; }
  .label--bottom-right { left: 683px; top: 2545px; }

  .vine-art {
    position: absolute;
    left: 0;
    top: 0;
    width: 424px;
    height: 300px;
  }

  .wordmark {
    position: absolute;
    right: 26px;
    top: 298px;
    text-align: right;
    line-height: 1;
  }
  .wordmark__name {
    display: block;
    font-family: "Stardos Stencil", "Arial Black", sans-serif;
    font-weight: 700;
    font-size: 60px;
    letter-spacing: 1px;
  }
  .wordmark__vintage {
    display: block;
    margin-top: 10px;
    font-family: "Arimo", Arial, sans-serif;
    font-size: 42px;
  }
  .label--white .wordmark { color: var(--label-blue); }
  .label--blue .wordmark  { color: var(--label-white); }
</style>
</head>
<body>
<main class="range">

  <svg width="0" height="0" style="position:absolute">
    <defs>
      <linearGradient id="glass" x1="0" x2="1" y1="0" y2="0">
        <stop offset="0" stop-color="var(--glass-edge)"/>
        <stop offset="0.3" stop-color="var(--glass-mid)"/>
        <stop offset="0.5" stop-color="var(--glass-light)"/>
        <stop offset="0.75" stop-color="var(--glass-mid)"/>
        <stop offset="1" stop-color="var(--glass-edge)"/>
      </linearGradient>
      <linearGradient id="glass-base" x1="0" x2="0" y1="0" y2="1">
        <stop offset="0" stop-color="var(--glass-base)" stop-opacity="0"/>
        <stop offset="1" stop-color="var(--glass-base)" stop-opacity="0.9"/>
      </linearGradient>
      <linearGradient id="capsule" x1="0" x2="1" y1="0" y2="0">
        <stop offset="0" stop-color="var(--cap-blue-dark)"/>
        <stop offset="0.45" stop-color="var(--cap-blue)"/>
        <stop offset="1" stop-color="var(--cap-blue-dark)"/>
      </linearGradient>
      <linearGradient id="capsule-art" x1="0" x2="1" y1="0" y2="1">
        <stop offset="0" stop-color="#ffffff"/>
        <stop offset="1" stop-color="#dfe9f3"/>
      </linearGradient>
      <linearGradient id="vine-gold" x1="0" x2="1" y1="0" y2="1">
        <stop offset="0" stop-color="var(--vine-gold-light)"/>
        <stop offset="1" stop-color="var(--vine-gold-dark)"/>
      </linearGradient>
      <linearGradient id="vine-blue" x1="0" x2="1" y1="0" y2="1">
        <stop offset="0" stop-color="var(--vine-blue-light)"/>
        <stop offset="1" stop-color="var(--vine-blue-dark)"/>
      </linearGradient>
      <linearGradient id="vine-white" x1="0" x2="1" y1="0" y2="1">
        <stop offset="0" stop-color="var(--vine-white-light)"/>
        <stop offset="1" stop-color="var(--vine-white-dark)"/>
      </linearGradient>
      <symbol id="bottle-shape" viewBox="0 0 460 1490">
        <path d="M150,300 L150,470 C150,620 10,700 10,880 L10,1450 Q10,1490 50,1490 L410,1490 Q450,1490 450,1450 L450,880 C450,700 310,620 310,470 L310,300 Z" fill="url(#glass)"/>
        <path d="M10,1300 L450,1300 L450,1450 Q450,1490 410,1490 L50,1490 Q10,1490 10,1450 Z" fill="url(#glass-base)"/>
        <rect x="148" y="0" width="164" height="318" rx="14" fill="url(#capsule)"/>
        <rect x="148" y="40" width="164" height="4" fill="var(--cap-blue-dark)"/>
        <text class="capsule-name" x="230" y="100" text-anchor="middle">WILD MO'S</text>
        <path d="M176,122 L290,118 L272,150 L246,170 L236,230 L214,262 L196,240 L184,190 Z" fill="url(#capsule-art)" role="img" aria-label="Small white grape bunch and leaf on the capsule"/>
      </symbol>
    </defs>
  </svg>

  <div class="bottle bottle--top-left"><svg width="460" height="1490"><use href="#bottle-shape"/></svg></div>
  <div class="bottle bottle--top-right"><svg width="460" height="1490"><use href="#bottle-shape"/></svg></div>
  <div class="bottle bottle--bottom-left"><svg width="460" height="1490"><use href="#bottle-shape"/></svg></div>
  <div class="bottle bottle--bottom-right"><svg width="460" height="1490"><use href="#bottle-shape"/></svg></div>

  <section class="label label--white label--top-left">
    <svg class="vine-art" viewBox="0 0 424 300" role="img" aria-label="Gold grape bunch and vine leaf hanging from a branch">
      <path d="M0,0 H424 V40 L400,60 L385,135 L345,165 L305,125 L255,95 L205,125 L150,205 L95,262 L45,290 L0,280 Z" fill="url(#vine-gold)"/>
    </svg>
    <div class="wordmark">
      <span class="wordmark__name">WILD MO'S</span>
      <span class="wordmark__vintage">2012</span>
    </div>
  </section>

  <section class="label label--blue label--top-right">
    <svg class="vine-art" viewBox="0 0 424 300" role="img" aria-label="Gold grape bunch and vine leaf hanging from a branch">
      <path d="M0,0 H424 V40 L400,60 L385,135 L345,165 L305,125 L255,95 L205,125 L150,205 L95,262 L45,290 L0,280 Z" fill="url(#vine-gold)"/>
    </svg>
    <div class="wordmark">
      <span class="wordmark__name">WILD MO'S</span>
      <span class="wordmark__vintage">2012</span>
    </div>
  </section>

  <section class="label label--white label--bottom-left">
    <svg class="vine-art" viewBox="0 0 424 300" role="img" aria-label="Blue grape bunch and vine leaf hanging from a branch">
      <path d="M0,0 H424 V40 L400,60 L385,135 L345,165 L305,125 L255,95 L205,125 L150,205 L95,262 L45,290 L0,280 Z" fill="url(#vine-blue)"/>
    </svg>
    <div class="wordmark">
      <span class="wordmark__name">WILD MO'S</span>
      <span class="wordmark__vintage">2012</span>
    </div>
  </section>

  <section class="label label--blue label--bottom-right">
    <svg class="vine-art" viewBox="0 0 424 300" role="img" aria-label="White grape bunch and vine leaf hanging from a branch">
      <path d="M0,0 H424 V40 L400,60 L385,135 L345,165 L305,125 L255,95 L205,125 L150,205 L95,262 L45,290 L0,280 Z" fill="url(#vine-white)"/>
    </svg>
    <div class="wordmark">
      <span class="wordmark__name">WILD MO'S</span>
      <span class="wordmark__vintage">2012</span>
    </div>
  </section>

</main>
</body>
</html>
```